Flyer for American Indian Elders on Dementia Warning Signs

We need a flyer designed for older adults who are American Indian or Alaska Native (in the U.S.).

Ideally, the flyer should complement the colors of our logos. The project logo and our organization logo are attached to the brief.

When people see the flyer we want them to feel that it represents their culture, is warm, and professional but relatable to older adults and people who have limited incomes.

I have attached an earlier draft of the document we designed ourselves BUT we want different and better.

It is for older adults who have trouble reading so:
1. you must use a font that is 11.5 points or larger
2. Do not put text over complex pictures or use shading with words
3. You can use a serif font for the heading, but should use san serif for the body text
4. There should be good contrast between the font color and background

Please do not use any images that include a head dress or pictures of American Indian people or things that are very traditional or "token" imagery.

We need to save a small space under the call out box/ somewhere on the flyer for other people to add their logo once they download.

Let us know if you have questions or need additional information.

Target Market(s)

Older American Indian people

Font styles to use
Serif
Sans Serif

Requirements
Must have
• Easy to read for older adults
Should not have
• indian headdress

```html
<!DOCTYPE html>
<html lang="en">
<head>
<meta charset="utf-8">
<title>10 Signs of Thinking or Memory Changes</title>
<link href="https://fonts.googleapis.com/css2?family=Montserrat:wght@500;700&family=Hind:wght@400;600&family=Roboto+Condensed:ital,wght@1,600&display=swap" rel="stylesheet">
<style>
:root{
  --navy:#1c3557;
  --navy-deep:#1f3a5c;
  --slate:#40607f;
  --wave-light:#a3adb9;
  --wave-mid:#6f8198;
  --white:#ffffff;
  --teal:#4ea7ac;
  --brick:#ac5a55;
  --footer:#3d5a7a;
}
*{margin:0;padding:0;box-sizing:border-box}
html,body{width:848px;height:1200px;overflow:hidden;background:var(--white)}
body{font-family:"Hind",sans-serif;color:var(--navy);position:relative}
.title{position:absolute;top:40px;left:0;width:848px;text-align:center;font-family:"Montserrat",sans-serif;font-weight:500;font-size:43px;line-height:46px;color:var(--navy)}
.title b{font-weight:700}
.intro{position:absolute;left:12px;width:824px;text-align:center;font-weight:600;font-size:15.5px;line-height:20px;color:var(--navy)}
.intro.one{top:150px}
.intro.two{top:210px}
.wave{position:absolute;top:255px;left:0;width:848px;height:60px}
.signs{position:absolute;top:308px;left:0;width:848px;height:738px;background:linear-gradient(180deg,var(--navy-deep) 0%,var(--slate) 100%);color:var(--white)}
.sign{position:absolute;width:340px;font-size:15.5px;line-height:19.7px}
.sign .num{position:absolute;left:-45px;top:-4px;width:28px;height:28px;border-radius:50%;background:var(--white);color:var(--navy);font-weight:600;font-size:15px;line-height:30px;text-align:center}
.sign h3{font-size:15.5px;font-weight:600;line-height:19.7px}
.sign h3 span{font-weight:400}
.sign p{margin-top:4px}
.sign ul{list-style:none;margin-top:5px}
.sign li{position:relative}
.sign li::before{content:"";position:absolute;left:-37px;top:6px;width:7px;height:7px;border-radius:50%;background:var(--white)}
.left{left:80px}.right{left:480px;width:345px}
.points{position:absolute;left:458px;top:444px;width:366px}
.points h2{background:var(--brick);color:var(--white);font-family:"Montserrat",sans-serif;font-weight:700;font-size:19px;text-align:center;height:31px;line-height:31px;border-radius:2px}
.point{margin-top:8px;height:47px;display:flex;align-items:center;justify-content:center;text-align:center;font-family:"Roboto Condensed",sans-serif;font-style:italic;font-weight:600;font-size:15px;line-height:18px;color:var(--white);padding:0 10px;border-radius:2px}
.point.teal{background:var(--teal)}.point.brick{background:var(--brick)}
.partners{position:absolute;top:1046px;left:0;width:848px;height:82px}
.partner{position:absolute;top:22px;display:flex;align-items:center;gap:10px;font-family:"Montserrat",sans-serif;font-weight:700;font-size:17px;line-height:19px}
.partner .mark{width:38px;height:38px;border-radius:50%;flex:none}
.partner.one{left:82px;color:var(--teal)}
.partner.one .mark{background:var(--teal)}
.partner.two{left:480px;color:var(--brick)}
.partner.two .mark{border-radius:0;background:var(--brick)}
.learn{position:absolute;top:1128px;left:0;width:848px;height:72px;background:var(--footer);color:var(--white);text-align:center}
.learn p{font-weight:600;font-size:16px;letter-spacing:.4px;margin-top:10px}
.links{display:flex;justify-content:center;align-items:center;gap:30px;font-size:14.5px;margin-top:4px;letter-spacing:.4px}
.links .bar{width:2px;height:20px;background:var(--white)}
</style>
</head>
<body>
<h1 class="title"><b>10 Signs</b> of Thinking or Memory<br>changes <b>that might dementia</b></h1>
<p class="intro one">As we get older, we may slow down a bit. This is a normal part of aging. Changes in memory or thinking that make it harder to get through the day, are not a normal part of aging. These may be early signs of dementia.</p>
<p class="intro two">Because American Indian and Alaska Native people have a high risk of dementia, it is important to know the warning signs. Do you have any of these 10 signs? If so, talk to your doctor.</p>

<svg class="wave" viewBox="0 0 848 60" preserveAspectRatio="none" aria-hidden="true">
  <path d="M0 14 C120 50 260 50 430 34 C600 18 740 5 848 14 L848 60 L0 60 Z" fill="var(--wave-light)"/>
  <path d="M0 30 C150 60 300 55 450 42 C620 28 760 22 848 36 L848 60 L0 60 Z" fill="var(--wave-mid)"/>
  <path d="M0 44 C160 60 320 60 470 52 C640 44 770 42 848 50 L848 60 L0 60 Z" fill="var(--navy-deep)"/>
</svg>

<section class="signs">
  <div class="sign left" style="top:22px">
    <span class="num">1</span>
    <h3>Memory loss that affects your daily life. You may:</h3>
    <ul><li>Forget events or important dates</li><li>Repeat yourself</li><li>Rely more often on lists or sticky notes to remember things more often</li></ul>
  </div>
  <div class="sign left" style="top:166px;width:350px">
    <span class="num">2</span>
    <h3>Sudden Trouble planning or solving problems. You may have a harder time:</h3>
    <p>Paying bills<br>Cooking recipes you have used for years</p>
  </div>
  <div class="sign left" style="top:271px">
    <span class="num">3</span>
    <h3>You get Get confused about the time, date, or where you are</h3>
  </div>
  <div class="sign left" style="top:330px">
    <span class="num">4</span>
    <h3>Daily tasks are getting harder, including:</h3>
    <ul><li>Driving</li><li>Making a grocery list or going shopping</li></ul>
  </div>
  <div class="sign left" style="top:416px;width:350px">
    <span class="num">5</span>
    <h3>Trouble with how your eyesight and thinking work together that gets worse. This includes:</h3>
    <ul><li>Tripping, falls, or problems with your balance</li><li>Spilling or dropping things more</li></ul>
  </div>
  <div class="sign left" style="top:520px">
    <span class="num">6</span>
    <h3>New trouble talking or writing</h3>
    <p>You have a hard time finding the words you want to say.</p>
    <p>For example, you may say “that thing on your wrist that tells time” instead of “watch.”</p>
  </div>
  <div class="sign left" style="top:650px;width:350px">
    <span class="num">7</span>
    <h3>Lose and cannot find things. <span>For example, you:</span></h3>
    <ul><li>Can’t find the coffee pot that you use every day</li><li>Might put your car keys in the freezer</li></ul>
  </div>

  <div class="sign right" style="top:22px">
    <span class="num">8</span>
    <h3>Notice changes in mood or personality, <span>such as being:</span></h3>
    <ul><li>Easily mad or sad in everyday situations</li><li>More fearful (scared) or suspicious (not trusting)</li></ul>
  </div>
  <div class="sign right" style="top:127px">
    <span class="num">9</span>
    <h3>Act different and make poor choices. <span>This may make you more likely to:</span></h3>
    <ul><li>Spend money you do not have or be a scam victim</li><li>Stop washing up regularly or pay less attention to how you look</li><li>Forget to take care of your pet</li></ul>
  </div>
  <div class="sign right" style="top:291px">
    <span class="num">10</span>
    <h3>Pull away from friends and family because it is harder to keep up.</h3>
    <p style="margin-top:0">You may not want to do things you used to enjoy, like sporting events, church, music, or sex.</p>
  </div>

  <aside class="points">
    <h2>Main Points</h2>
    <p class="point teal">American Indian and Alaska Native people have a higher risk of dementia. than White people.</p>
    <p class="point brick">Big changes in memory or thinking that make it hard to get through the day are not a normal part of aging.</p>
    <p class="point teal">People with one or more of these 10 signs should talk to their doctor to find the cause. It is not always dementia.</p>
    <p class="point brick">Early dementia diagnosis gives you a chance to get care and plan your future.</p>
  </aside>
</section>

<footer class="partners">
  <div class="partner one"><span class="mark"></span><span>NORTHWIND CENTER<br>FOR BRAIN HEALTH</span></div>
  <div class="partner two"><span class="mark"></span><span>CIRCLE COUNCIL ON<br>ELDER WELLNESS</span></div>
</footer>

<section class="learn">
  <p>To learn more about the warning signs of dementia in American Indian and Alaska Native people, visit:</p>
  <div class="links"><span>www.northwindbrainhealth.org</span><span class="bar"></span><span>www.circleelderwell.org/aging</span></div>
</section>
</body>
</html>
```